business card for a massage therapy practice named 'Meadow and Willow Massage Studio'

I really need a trendy, yet easy on the eyes business card to complement my logo. Ideally with some gold or rose gold foil work.

My uploaded file of the logo I have in horizontal but I have a vertical version as well. Another color that is used in the website is a blush pink here and there. I'd like to see some trendy tropical leaves in the design.

```html
<!DOCTYPE html>
<html lang="en">
<head>
<meta charset="utf-8">
<title>Meadow and Willow Massage Studio — Business Card</title>
<link href="https://fonts.googleapis.com/css2?family=Open+Sans:wght@400;600&family=Kaushan+Script&display=swap" rel="stylesheet">
<style>
  :root {
    --backdrop: #2a2a2a;
    --card: #111111;
    --card-edge: #1a1a1a;
    --mint: #7fd9c1;
    --gold: #a8935a;
    --ink-light: #e6e6e6;
    --ink-soft: #cfcfcf;
    --rule: #5c5c5c;
  }
  * { margin: 0; padding: 0; box-sizing: border-box; }
  html, body { width: 1200px; height: 900px; overflow: hidden; }
  body {
    background: var(--backdrop);
    font-family: "Open Sans", Arial, sans-serif;
    position: relative;
  }
  .card {
    position: absolute;
    left: 280px;
    width: 640px;
    height: 366px;
    background: linear-gradient(160deg, var(--card-edge), var(--card));
    overflow: hidden;
  }
  .card::after {
    content: "";
    position: absolute;
    left: 0; right: 0; bottom: 0;
    height: 12px;
    background: var(--mint);
  }
  .card--front { top: 72px; }
  .card--back { top: 468px; }

  /* Front */
  .brand {
    position: absolute;
    top: 92px;
    left: 0; right: 0;
    display: flex;
    justify-content: center;
    align-items: center;
    gap: 18px;
  }
  .brand__mark {
    width: 62px; height: 62px;
    border-radius: 50%;
    background: var(--gold);
    flex: none;
  }
  .brand__name {
    color: var(--ink-light);
    font-weight: 600;
    font-size: 30px;
    line-height: 1.15;
    letter-spacing: 0.5px;
  }
  .follow {
    position: absolute;
    top: 232px;
    left: 70px; right: 70px;
    display: flex;
    align-items: center;
    gap: 14px;
  }
  .follow__rule { flex: 1; height: 1px; background: var(--rule); }
  .follow__body { display: flex; flex-direction: column; align-items: center; gap: 8px; }
  .follow__label {
    color: var(--ink-soft);
    font-size: 13px;
    letter-spacing: 1.5px;
  }
  .follow__icons { display: flex; gap: 6px; }
  .follow__icons span {
    width: 18px; height: 18px;
    border-radius: 50%;
    background: var(--mint);
  }

  /* Back */
  .person {
    position: absolute;
    top: 92px;
    left: 36px;
    width: 266px;
    text-align: right;
  }
  .person__name {
    font-family: "Kaushan Script", cursive;
    color: var(--mint);
    font-size: 36px;
    font-weight: 400;
    line-height: 1.1;
    white-space: nowrap;
  }
  .person__role {
    color: var(--ink-soft);
    font-size: 17px;
    margin-top: 2px;
  }
  .divider {
    position: absolute;
    top: 104px;
    left: 320px;
    width: 1px;
    height: 58px;
    background: var(--rule);
  }
  .contact {
    position: absolute;
    top: 108px;
    left: 336px;
    width: 286px;
    list-style: none;
    color: var(--ink-light);
    font-size: 16px;
  }
  .contact li { display: flex; align-items: center; gap: 8px; line-height: 1.55; white-space: nowrap; }
  .contact svg { width: 15px; height: 15px; fill: var(--mint); flex: none; }
  .address {
    position: absolute;
    top: 232px;
    left: 0; right: 0;
    text-align: center;
    color: var(--ink-light);
    font-size: 17px;
  }
</style>
</head>
<body>

<section class="card card--front" aria-label="Card front">
  <div class="brand">
    <span class="brand__mark" aria-hidden="true"></span>
    <div class="brand__name">Meadow and Willow<br>Massage Studio</div>
  </div>
  <div class="follow">
    <span class="follow__rule"></span>
    <div class="follow__body">
      <span class="follow__label">FOLLOW US ON</span>
      <div class="follow__icons" aria-hidden="true"><span></span><span></span><span></span><span></span></div>
    </div>
    <span class="follow__rule"></span>
  </div>
</section>

<section class="card card--back" aria-label="Card back">
  <div class="person">
    <h1 class="person__name">Marisol Bennett</h1>
    <p class="person__role">Massage Theraphist</p>
  </div>
  <span class="divider"></span>
  <ul class="contact">
    <li>
      <svg viewBox="0 0 16 16" aria-hidden="true"><path d="M3.5 1.5l2.5 0 1.2 3-1.6 1.2c.8 1.8 2.2 3.2 4 4l1.2-1.6 3 1.2v2.5c0 .9-.7 1.6-1.6 1.6C6.6 13.4 2.6 9.4 2 3.1 1.9 2.2 2.6 1.5 3.5 1.5z"/></svg>
      (555) 201-7384
    </li>
    <li>
      <svg viewBox="0 0 16 16" aria-hidden="true"><path d="M1 3h14v1.2L8 9 1 4.2z M1 5.6l7 4.8 7-4.8V13H1z"/></svg>
      meadowandwillow@example.com
    </li>
  </ul>
  <p class="address">482 Linden Ave. suite 210 Fairview, CA 90210</p>
</section>

</body>
</html>
```